Business Card Design

Want something very unique. No business, just personal. The image I submitted is for inspiration only.

Target Market(s)

friends and new acquaintances

Industry/Entity Type

Business

Contact Information for Business Card

Nora Pettigrew
Mesa Linda, NM
505-771-4926
norapettigrew@quillmail.net

```html
<!DOCTYPE html>
<html lang="en">
<head>
<meta charset="utf-8">
<title>Nora Pettigrew — Business Card</title>
<link rel="stylesheet" href="https://fonts.googleapis.com/css2?family=Ubuntu:wght@400;700&display=swap">
<style>
  :root {
    --backdrop: #7c2329;
    --card-white: #ffffff;
    --card-shade: #ececec;
    --pattern-tone: #a9a9a9;
    --ink: #1a1a1a;
  }
  html, body {
    margin: 0;
    padding: 0;
    width: 1200px;
    height: 898px;
    overflow: hidden;
    background: var(--backdrop);
  }
  .canvas {
    position: relative;
    width: 1200px;
    height: 898px;
    display: flex;
    align-items: center;
    justify-content: center;
  }
  .business-card {
    position: relative;
    width: 900px;
    height: 514px;
    background: radial-gradient(ellipse at 50% 45%, var(--card-white) 0%, var(--card-white) 45%, var(--card-shade) 100%);
    overflow: hidden;
  }
  .pattern-band {
    position: absolute;
    left: 0;
    width: 100%;
    background: var(--pattern-tone);
  }
  .pattern-band--top {
    top: 0;
    height: 78px;
  }
  .pattern-band--bottom {
    bottom: 0;
    height: 118px;
  }
  .contact-block {
    position: absolute;
    top: 78px;
    bottom: 118px;
    left: 0;
    right: 0;
    display: flex;
    flex-direction: column;
    align-items: center;
    justify-content: center;
    font-family: "Ubuntu", sans-serif;
    color: var(--ink);
    text-align: center;
    line-height: 1.45;
  }
  .contact-name {
    margin: 0;
    font-size: 34px;
    font-weight: 700;
  }
  .contact-line {
    margin: 0;
    font-size: 32px;
    font-weight: 400;
  }
</style>
</head>
<body>
  <main class="canvas">
    <section class="business-card">
      <div class="pattern-band pattern-band--top" role="img" aria-label="Band of black polka dots on white"></div>
      <div class="contact-block">
        <p class="contact-name">Nora Pettigrew Mesa Linda, NM</p>
        <p class="contact-line">505-771-4926</p>
        <p class="contact-line">norapettigrew@quillmail.net</p>
      </div>
      <div class="pattern-band pattern-band--bottom" role="img" aria-label="Band of black polka dots on white"></div>
    </section>
  </main>
</body>
</html>
```